Web Design Project

We are looking for a new site design for the KELVO Canada. The current site can be found at
http://www.kelvocanada.example/
The URL is provided for reference. We want a completely different look and layout which is shown in the specifications document.
As part of the design, we want a home page, and inside page.
The design you provide will be implemented in Joomla. The design winner will only need to provide the PSD. We anticipate creating the template coding in-house.
However, if you have experience creating Joomla templates, please let us know as we may ask you to bid separately to do that phase of the project.
We've provided a specifications document which includes wireframes of the home page, and inside page. We've also included a logo file.
For the header at the top, as indicated in the specs document, we want to keep the same overall treatment to every page. We want a graphic treatment with the logo for the header area. In this manner, the design will be flexiable and can be used for future years.
For the home page, we've indicated that we'd like to have a slider implemented within the design.
The wireframe is provided to illustrate the placement of content and menu items. The exact dimensions of each component can be revised as you see fit. We are also flexiable if you feel we have missed items.

```html
<!DOCTYPE html>
<html lang="en">
<head>
<meta charset="utf-8">
<title>KELVO Canada</title>
<link href="https://fonts.googleapis.com/css2?family=Arimo:wght@400;700&display=swap" rel="stylesheet">
<style>
:root{
  --navy:#2d4a8c;
  --navy-dark:#1f3670;
  --red:#d0312f;
  --red-dark:#b3201f;
  --red-active:#a81c1c;
  --maroon:#a3191c;
  --text:#555;
  --panel:#f2f2f2;
  --line:#e2e2e2;
  --footer:#333;
  --footer-text:#d8d8d8;
}
*{box-sizing:border-box;margin:0;padding:0}
html,body{width:1200px;height:801px;overflow:hidden}
body{position:relative;background:#fff;font-family:"Arimo",Arial,sans-serif;color:var(--text)}
a{color:inherit;text-decoration:none}
ul{list-style:none}

.site-header{position:absolute;left:0;top:0;width:1200px;height:122px;
  background:linear-gradient(#fff 0,#fff 64px,#f7f7f7 65px,#f7f7f7 100%);border-top:4px solid var(--navy)}
.brand{position:absolute;left:66px;top:34px;display:flex;align-items:center;gap:10px;
  font-size:40px;font-weight:700;color:var(--navy);letter-spacing:1px}
.brand-dot{width:22px;height:22px;border-radius:50%;background:var(--red)}
.utility-nav{position:absolute;left:831px;top:0;width:302px;height:38px;background:var(--navy);
  border-radius:0 0 4px 4px;display:flex;align-items:center;justify-content:center;color:#fff;font-size:14.5px;gap:11px}

.main-nav{position:absolute;left:0;top:122px;width:1200px;height:45px;
  background:linear-gradient(#e03d3b,var(--red) 60%,#c92d2b)}
.main-nav ul{position:absolute;left:66px;top:0;display:flex;height:45px}
.main-nav li{height:45px;display:flex;align-items:center;justify-content:center;color:#fff;font-size:15px;
  border-right:1px solid var(--red-dark);border-left:1px solid #e45755}
.main-nav li.active{background:var(--red-active)}

.dropdown{position:absolute;left:177px;top:169px;width:119px;height:120px;background:var(--red-dark);
  border:1px solid #d64745;padding:7px 0 0 11px;z-index:3;color:#fff;font-size:12.5px}
.dropdown li{height:27px;line-height:27px}
.dropdown li::before{content:"•";margin-right:7px}

.slider-frame{position:absolute;left:66px;top:170px;width:1068px;height:119px;background:#eee}
.slider-image{position:absolute;left:71px;top:175px;width:1056px;height:109px;
  background:linear-gradient(#c6d3e0 0,#a9b7c6 45%,#6f7a85 100%)}
.slider-caption{position:absolute;left:749px;top:190px;width:351px;height:79px;background:#fff;border-radius:3px;
  padding:12px 22px;color:#111;font-size:15.5px;line-height:19px}
.slider-caption time{display:block;margin-top:3px;color:var(--red);font-size:12px;font-style:italic}
.slider-dots{position:absolute;left:82px;top:260px;display:flex;gap:10px}
.slider-dots span{width:12px;height:12px;border-radius:50%;border:2px solid #fff;background:#444}
.slider-dots span.current{background:var(--red)}

.sponsors{position:absolute;left:66px;top:298px;width:286px;height:128px;background:var(--panel);border:1px solid var(--line)}
.sponsors h2{height:37px;padding:9px 11px;font-size:17px;font-weight:400;color:var(--maroon);border-bottom:1px solid #ddd;position:relative}
.sponsors .arrows{position:absolute;right:16px;top:9px;color:#333;font-size:15px;font-weight:700;letter-spacing:3px}
.sponsor-logos{display:flex;justify-content:space-around;align-items:center;padding:14px 8px 0}
.sponsor-name{font-size:17px;font-weight:700;color:#444}
.sponsors .become{position:absolute;right:19px;bottom:10px;font-size:12.5px;color:var(--navy-dark);text-decoration:underline}

.member-login{position:absolute;left:66px;top:439px;width:286px;height:174px;
  background:linear-gradient(var(--navy),var(--navy-dark));border:1px solid #203a77;color:#fff}
.member-login h2{height:47px;padding:15px 0 0 54px;font-size:17px;font-weight:400;border-bottom:1px solid #4962a0;position:relative}
.member-login h2 svg{position:absolute;left:16px;top:5px}
.field{position:absolute;left:14px;font-size:12.5px;display:flex;align-items:center}
.field label{width:77px}
.field span{width:177px;height:25px;background:#fff;border-radius:3px;border:1px solid #ccc}
.login-button{position:absolute;right:15px;bottom:13px;width:69px;height:25px;border-radius:2px;background:linear-gradient(#fff,#d9d9d9);
  color:#222;font-size:12px;font-weight:700;display:flex;align-items:center;justify-content:center;border:1px solid #999}

.stay-connected{position:absolute;left:75px;top:633px;display:flex;align-items:center;color:var(--maroon);font-size:15px}
.stay-connected ul{display:flex;gap:8px;margin-left:26px}
.stay-connected li{width:27px;height:27px;border-radius:50%;background:var(--navy);display:flex;align-items:center;justify-content:center}

.welcome{position:absolute;left:365px;top:298px;width:768px;height:222px;background:var(--panel)}
.welcome h1{position:absolute;left:23px;top:17px;font-size:17px;font-weight:400;color:var(--maroon)}
.welcome p{position:absolute;left:24px;top:53px;width:484px;font-size:13px;line-height:21.5px;text-align:justify;color:#555}

.news{position:absolute;left:897px;top:307px;width:229px;height:199px;background:linear-gradient(#5a5a5a,#2a2a2a);border:1px solid #222;color:#fff}
.news h2{height:44px;padding:12px 0 0 52px;font-size:16.5px;font-weight:400;background:#555;border-bottom:1px solid #777;position:relative}
.news h2 i{position:absolute;left:15px;top:11px;width:27px;height:21px;background:linear-gradient(#d9e3ec,#9aa9b8);border:1px solid #eee}
.news h3{margin:13px 0 0 15px;font-size:13px;font-weight:400}
.news h3::before{content:"▸";font-size:10px;margin-right:12px}
.news p{margin:10px 14px 0 33px;font-size:11.5px;line-height:16px;color:#ddd}
.news .meta{margin:9px 0 0 33px;font-size:11.5px;color:#eee;word-spacing:2px}
.news .view-all{position:absolute;left:0;bottom:0;width:100%;height:34px;background:#262626;text-align:center;line-height:34px;font-size:11.5px;color:#bbb;text-decoration:underline}

.regions-title{position:absolute;left:367px;top:532px;font-size:17px;font-weight:400;color:var(--maroon)}
.region{position:absolute;top:564px;width:183px;height:153px;background:#fff;border:1px solid var(--line);
  box-shadow:inset 0 0 14px #ececec;padding:11px 0 0 20px}
.region h3{font-size:17px;font-weight:400;color:var(--navy);margin-bottom:8px}
.region li{font-size:12.5px;color:#444;height:27px;line-height:20px}
.region li::before{content:"•";color:#777;margin-right:6px}
.region li.tight{height:23px}

.site-footer{position:absolute;left:0;top:730px;width:1200px;height:71px;background:var(--footer);color:var(--footer-text);font-size:12.5px;text-align:center}
.site-footer nav{padding-top:16px;word-spacing:3px}
.site-footer p{margin-top:12px;word-spacing:3px}
</style>
</head>
<body>

<header class="site-header">
  <div class="brand"><span class="brand-dot"></span>KELVO</div>
  <nav class="utility-nav"><a>Home</a>|<a>Contact us</a>|<a>KELVO International</a></nav>
</header>

<nav class="main-nav">
  <ul>
    <li class="active" style="width:111px">About</li>
    <li style="width:120px">Board</li>
    <li style="width:136px">Chapters</li>
    <li style="width:182px">Member Space</li>
    <li style="width:244px">Resources &amp; Knowledge</li>
    <li style="width:166px">Sponsorship</li>
    <li style="width:109px">Exhibit</li>
  </ul>
</nav>

<ul class="dropdown">
  <li>Sample Link 1</li><li>Sample Link 2</li><li>Sample Link 3</li><li>Sample Link 4</li>
</ul>

<section class="slider">
  <div class="slider-frame"></div>
  <div class="slider-image" role="img" aria-label="City skyline with office towers under a pale sky"></div>
  <div class="slider-caption">Nam ut sem nec sem varius scelerisque at a arcu. Mauris ac nisi nisi.<time>Jan 10, 2013</time></div>
  <div class="slider-dots"><span class="current"></span><span></span><span></span><span></span></div>
</section>

<aside class="sponsors">
  <h2>Sponsors<span class="arrows">‹›</span></h2>
  <div class="sponsor-logos">
    <span class="sponsor-name">Dealhaven</span>
    <span class="sponsor-name">Savewell Network</span>
  </div>
  <a class="become">Become a sponsor</a>
</aside>

<aside class="member-login">
  <h2>
    <svg width="26" height="34" viewBox="0 0 26 34"><path d="M6 15V10a7 7 0 0 1 14 0v5" fill="none" stroke="#ccc" stroke-width="3"/><rect x="2" y="14" width="22" height="18" rx="2" fill="#bbb"/></svg>
    Member Login
  </h2>
  <div class="field" style="top:64px"><label>Username :</label><span></span></div>
  <div class="field" style="top:102px"><label>Password :</label><span></span></div>
  <div class="login-button">LOG IN</div>
</aside>

<div class="stay-connected">
  Stay Connected
  <ul>
    <li></li><li></li><li></li>
    <li><svg width="15" height="11" viewBox="0 0 15 11"><rect x="0.75" y="0.75" width="13.5" height="9.5" fill="none" stroke="#fff" stroke-width="1.5"/><path d="M1 1l6.5 5 6.5-5" fill="none" stroke="#fff" stroke-width="1.5"/></svg></li>
  </ul>
</div>

<main class="welcome">
  <h1>Welcome to our stie</h1>
  <p>Nulla at vestibulum magna. Curabitur consectetur eros vitae elit faucibus sit amet sagittis purus congue. In porta eleifend risus quis suscipit. Etiam elit neque, sagittis non vehicula vitae, aliquam ac nunc. Mauris augue nulla, cursus vel tincidunt a, rhoncus vel elit. Integer bibendum, massa laoreet tincidunt convallis, turpis dolor sollicitudin orci, quis sodales nisl magna et leo. Vestibulum sed est vel nunc commodo placerat. faucibus id, tristique id est.</p>
</main>

<section class="news">
  <h2><i></i>News and Events</h2>
  <h3>Frozen Door</h3>
  <p>Nulla facilisi. Curabitur at elit ligula, eget kot hen drerit felis vehicula avdal.</p>
  <div class="meta">Dec-26-2012 &nbsp; | &nbsp; Read more</div>
  <a class="view-all">View all News and Events</a>
</section>

<h2 class="regions-title">Regions</h2>
<section class="region" style="left:366px">
  <h3>Mountain Pacific</h3>
  <ul><li>Vancouver Island</li><li>Vancouver</li><li>Calgary</li></ul>
</section>
<section class="region" style="left:558px">
  <h3>Western</h3>
  <ul><li>Edmonton</li><li>Saskatchewan</li><li>Winnipeg</li></ul>
</section>
<section class="region" style="left:751px">
  <h3>Central</h3>
  <ul><li>National Capital-Ottawa</li><li>Southwestern Ontario</li><li class="tight">Montreal</li><li>Toronto</li></ul>
</section>
<section class="region" style="left:943px">
  <h3>Atlantic</h3>
  <ul><li>Nova Scotia</li><li>Terra-Nova, St. John’s</li><li class="tight">Prince Edward Island</li><li>Atlantic, St. John’s</li></ul>
</section>

<footer class="site-footer">
  <nav>Home &nbsp;|&nbsp; About &nbsp;|&nbsp; Board &nbsp;|&nbsp; Chapters &nbsp;|&nbsp; Member Space &nbsp;|&nbsp; Resources &amp; Knowledge &nbsp;|&nbsp; Sponsorship &nbsp;|&nbsp; Exhibit &nbsp; | &nbsp;Member Login &nbsp;|&nbsp; Contact Us</nav>
  <p>Privacy Policy &nbsp;|&nbsp; Copyright © 2013 www.kelvo.example &nbsp;All rights reserved</p>
</footer>

</body>
</html>
```